I need a wordpress website for myconsulting company specialized in data privacy

I'm looking for a wordpress website for my consulting company specialized in data privacy (GDPR) and computer science.
The website will serve as entry point to for potential clients.
The website should have the following sections (I'm opened to new ideas):
- Presentation of the company
- General presentation
- Services provided with some details
- Blog/articles with tags (if possible)
- Contact
On every page of the website there should be some references to pages (such as privacy policy, legal information...)
If possible he website should be multinlingual (english and french). I'll personnally take care of the translation in french.
Regarding branding;
- Name of the company: Étienne Roubaud Conseil
- Logo is attached
- For colors to be used see attached PDF for exemple

```html
<!DOCTYPE html>
<html lang="en">
<head>
<meta charset="utf-8">
<title>Étienne Roubaud Conseil</title>
<link href="https://fonts.googleapis.com/css2?family=Michroma&family=Barlow:wght@400;500;600&display=swap" rel="stylesheet">
<style>
:root{
  --navy:#0b3550;
  --navy-dark:#0a2c43;
  --teal:#138a9c;
  --teal-light:#1fa7b8;
  --ink:#1d2a33;
  --muted:#4b5660;
  --line:#d9e2e6;
  --white:#ffffff;
}
*{box-sizing:border-box;margin:0;padding:0}
html,body{width:1200px;height:3450px;overflow:hidden}
body{position:relative;background:var(--white);font-family:"Barlow",sans-serif;color:var(--ink)}
.abs{position:absolute}
.display{font-family:"Michroma",sans-serif;font-weight:400}
.accent{color:var(--teal)}
.btn{position:absolute;background:var(--teal);color:var(--white);font-size:15px;font-weight:600;letter-spacing:.5px;display:flex;align-items:center;justify-content:center;border-radius:2px;box-shadow:0 3px 6px rgba(0,0,0,.15)}

/* header */
.brand{position:absolute;display:flex;align-items:center;gap:10px}
.brand-mark{width:26px;height:26px;border:3px solid var(--teal)}
.brand-name{font-size:17px;font-weight:500;color:var(--navy);line-height:1.15}
.brand-name small{display:block;font-size:10px;letter-spacing:6px}
.nav{position:absolute;top:42px;left:632px;display:flex;gap:40px;font-size:14px;color:var(--ink)}
.nav .active{color:var(--navy);border-bottom:2px solid var(--teal);padding-bottom:4px}
.lang{position:absolute;left:986px;top:33px;width:52px;height:33px;background:var(--teal);color:#fff;font-size:14px;display:flex;align-items:center;justify-content:center;gap:6px;border-radius:2px}

/* hero */
.hero-title{position:absolute;top:298px;left:0;width:1200px;text-align:center;color:#fff;font-size:30px;line-height:40px}

/* section heads */
.sec-head{position:absolute;left:0;width:1200px;text-align:center;font-size:30px;color:var(--navy)}
.sec-rule{position:absolute;left:585px;width:30px;height:2px;background:var(--teal)}

/* about */
.about-kicker{font-size:17px;color:var(--navy)}
.about-title{font-size:31px;color:var(--navy)}
.about-sub{font-size:12px;letter-spacing:6px;color:var(--teal);display:flex;align-items:center;gap:8px}
.about-sub span.rule{display:block;height:1px;background:var(--teal)}
.about-lead{font-size:14px;font-weight:600;color:var(--navy);line-height:21px}
.about-body{font-size:14px;color:var(--ink);line-height:27px}

/* services */
.svc{position:absolute;width:420px;height:185px}
.svc-card{position:absolute;left:70px;top:0;width:350px;height:185px;background:#fff;box-shadow:0 6px 18px rgba(11,53,80,.10);border-radius:4px}
.svc-photo{position:absolute;left:0;top:5px;width:158px;height:158px;border-radius:50%;border:2px solid #fff;box-shadow:0 0 0 2px var(--teal)}
.svc-text{position:absolute;left:181px;top:16px;width:225px}
.svc-text h3{font-family:"Michroma",sans-serif;font-weight:400;font-size:12px;color:var(--navy);margin-bottom:8px}
.svc-text p{font-size:12px;line-height:21.5px;color:var(--ink);letter-spacing:.3px}
.svc-text a{display:inline-block;margin-top:8px;margin-left:4px;font-size:15px;font-weight:500;color:var(--teal);text-decoration:underline}

/* blog */
.post{position:absolute;top:2009px;width:270px;height:369px;background:#fff}
.post-photo{width:270px;height:192px}
.post-body{padding:18px 16px}
.post-date{font-size:13px;color:var(--muted)}
.post-title{font-size:17px;font-weight:500;line-height:21px;margin:8px 0 14px;letter-spacing:.4px}
.post-ex{font-size:14px;line-height:20px;color:var(--muted);letter-spacing:.4px}
.post.featured{background:var(--navy)}
.post.featured .post-date,.post.featured .post-title{color:#fff}
.post.featured .post-ex{color:#c9d6de}

/* partners */
.partner{position:absolute;top:2548px;width:160px;height:70px;background:#fff;box-shadow:0 4px 14px rgba(0,0,0,.08);display:flex;align-items:center;justify-content:center;gap:8px;font-size:22px;font-weight:600;color:var(--navy)}
.partner i{width:16px;height:16px;border-radius:50%;background:var(--teal);display:block}

/* contact */
.field{position:absolute;border:1px solid var(--line);display:flex;align-items:flex-start;gap:10px;padding:15px 16px;font-size:13px;color:var(--ink)}
.field svg{flex:none;margin-top:1px}

/* footer */
.fnav{position:absolute;top:3241px;left:164px;display:flex;gap:44px;font-size:14px;color:var(--ink)}
.fnav .active{color:var(--teal)}
.social{position:absolute;top:3238px;width:30px;height:30px;border:1px solid var(--teal);display:flex;align-items:center;justify-content:center}
.social i{width:8px;height:8px;background:var(--teal);display:block}
.finfo{position:absolute;top:3314px;display:flex;gap:12px;font-size:13px;line-height:22px;color:var(--ink)}
.copy{position:absolute;top:3412px;left:393px;font-size:13px;font-weight:500;color:#fff}
</style>
</head>
<body>

<!-- header -->
<div class="brand" style="left:160px;top:22px">
  <span class="brand-mark"></span>
  <div class="brand-name">Étienne Roubaud<small>CONSEIL</small></div>
</div>
<nav class="nav">
  <span class="active">Home</span><span>Services</span><span>Blogs</span><span>Contact Us</span>
</nav>
<div class="lang">En
  <svg width="10" height="6" viewBox="0 0 10 6"><path d="M1 1l4 4 4-4" stroke="#fff" fill="none" stroke-width="1.5"/></svg>
</div>

<!-- hero -->
<svg class="abs" style="left:0;top:100px" width="1200" height="572" role="img" aria-label="Hero image: hand touching a digital network of security and data icons">
  <defs>
    <radialGradient id="heroGlow" cx="50%" cy="35%" r="70%">
      <stop offset="0" stop-color="#1d5f7d"/>
      <stop offset=".55" stop-color="#0f4663"/>
      <stop offset="1" stop-color="#0a2d45"/>
    </radialGradient>
  </defs>
  <path d="M0 0H1200V490L600 570L0 490Z" fill="#138a9c"/>
  <path d="M0 0H1200V485L600 562L0 485Z" fill="url(#heroGlow)"/>
</svg>
<h1 class="hero-title display">We Specialize In Data Privacy (GDPR)<br>&amp; Computer Science Consultancy</h1>
<div class="btn" style="left:520px;top:392px;width:158px;height:44px;font-weight:500;font-size:14px">CONTACT US</div>

<!-- about -->
<svg class="abs" style="left:155px;top:735px" width="380" height="380">
  <circle cx="190" cy="185" r="178" fill="none" stroke="#138a9c" stroke-width="2"/>
  <circle cx="192" cy="7" r="5" fill="#138a9c"/><circle cx="336" cy="94" r="5" fill="#138a9c"/>
  <circle cx="345" cy="260" r="5" fill="#138a9c"/><circle cx="214" cy="363" r="5" fill="#138a9c"/>
  <circle cx="57" cy="310" r="5" fill="#138a9c"/><circle cx="41" cy="81" r="5" fill="#138a9c"/>
</svg>
<div class="abs" role="img" aria-label="Photo of consultants working at computer screens" style="left:172px;top:754px;width:340px;height:340px;border-radius:50%;background:linear-gradient(135deg,#c79a6c 0%,#5c4a3a 45%,#1f3a3f 100%)"></div>
<div class="abs" style="left:418px;top:990px;width:100px;height:100px;border-radius:50%;background:#fff;box-shadow:0 4px 14px rgba(0,0,0,.2);display:flex;align-items:center;justify-content:center">
  <span style="width:40px;height:40px;border:5px solid var(--teal);display:block"></span>
</div>
<div class="abs about-kicker display" style="left:589px;top:770px">About</div>
<div class="abs about-title display" style="left:586px;top:790px">Étienne Roubaud</div>
<div class="abs about-sub" style="left:586px;top:828px"><span class="rule" style="width:110px"></span>CONSEIL<span class="rule" style="width:76px"></span></div>
<p class="abs about-lead" style="left:585px;top:863px;width:450px">Lorem ipsum dolor sit amet, consectetuer adipiscing elitsed diam nonummy nibh euismod tincidunt</p>
<p class="abs about-body" style="left:585px;top:912px;width:460px">Lorem ipsum dolor sit amet, consectetuer adipiscing elit, sed diam nonummy nibh euismod tincidunt ut laoreet dolore magna aliquam erat volutpat. Ut wisi enim ad minim veniam, quis nostrud exerci tation ullamcorper suscipit lobortis nisl ut aliquip ex ea commodo consequat. Duis autem vel eum iriure dolor in hendrerit in vulputate velit esse molestie consequat, vel illum dolore.</p>

<!-- services -->
<div class="sec-rule" style="top:1219px"></div>
<h2 class="sec-head display" style="top:1232px">Our <span class="accent">Services</span></h2>

<div class="svc" style="left:160px;top:1310px">
  <div class="svc-card"></div>
  <div class="svc-photo" role="img" aria-label="Digital hand typing on a keyboard" style="background:radial-gradient(circle at 40% 35%,#9fd8f5,#1f5fa6 45%,#0a1f45)"></div>
  <div class="svc-text"><h3>Computer Science</h3><p>Lorem ipsum dolor sit amet consec adipiscing elit sed diam nonummy nibhrti euismod tincidunt ut laoreet dolore magna aliqua merat.</p><a>Read More</a></div>
</div>
<div class="svc" style="left:618px;top:1310px">
  <div class="svc-card"></div>
  <div class="svc-photo" role="img" aria-label="Person at a laptop with data security overlay" style="background:radial-gradient(circle at 50% 40%,#4fa7a0,#1c3a3f 55%,#0d1a1f)"></div>
  <div class="svc-text"><h3>Data Privacy (GDPR)</h3><p>Lorem ipsum dolor sit amet consec adipiscing elit sed diam nonummy nibhrti euismod tincidunt ut laoreet dolore magna aliqua merat.</p><a>Read More</a></div>
</div>
<div class="svc" style="left:160px;top:1545px">
  <div class="svc-card"></div>
  <div class="svc-photo" role="img" aria-label="Source code on a dark screen" style="background:linear-gradient(135deg,#3a3a3a,#1b1b1b)"></div>
  <div class="svc-text"><h3>Data Encryption Solutions</h3><p>Lorem ipsum dolor sit amet consec adipiscing elit sed diam nonummy nibhrti euismod tincidunt ut laoreet dolore magna aliqua merat.</p><a>Read More</a></div>
</div>
<div class="svc" style="left:618px;top:1545px">
  <div class="svc-card"></div>
  <div class="svc-photo" role="img" aria-label="Monitor showing a security shield" style="background:radial-gradient(circle at 40% 40%,#3f9a92,#173a44 60%,#10202a)"></div>
  <div class="svc-text"><h3>Ransomware Protection</h3><p>Lorem ipsum dolor sit amet consec adipiscing elit sed diam nonummy nibhrti euismod tincidunt ut laoreet dolore magna aliqua merat.</p><a>Read More</a></div>
</div>
<div class="btn" style="left:539px;top:1774px;width:120px;height:36px">View All</div>

<!-- blog -->
<div class="sec-rule" style="top:1927px"></div>
<h2 class="sec-head display" style="top:1940px">Latest <span class="accent">Blog Posts</span></h2>

<article class="post" style="left:161px">
  <div class="post-photo" role="img" aria-label="Team joining hands over a digital ring" style="background:linear-gradient(135deg,#7fa8d6,#3f5f9a 55%,#27375f)"></div>
  <div class="post-body"><div class="post-date">22 Feb, 2022</div><h3 class="post-title">Lorem ipsum dolor sit ame consectetuer adipi</h3><p class="post-ex">Lorem ipsum dolor sit amet, consectetuer adipiscing elit, sed diam nonummy nibh</p></div>
</article>
<article class="post featured" style="left:465px">
  <div class="post-photo" role="img" aria-label="Consultants working at computer screens" style="background:linear-gradient(135deg,#c79a6c,#5c4a3a 45%,#1f3a3f)"></div>
  <div class="post-body"><div class="post-date">22 Feb, 2022</div><h3 class="post-title">Lorem ipsum dolor sit ame consectetuer adipi</h3><p class="post-ex">Lorem ipsum dolor sit amet, consectetuer adipiscing elit, sed diam nonummy nibh</p></div>
</article>
<article class="post" style="left:767px">
  <div class="post-photo" role="img" aria-label="Business team meeting around a table with laptops" style="background:linear-gradient(135deg,#e6e6e6,#b9bcc0 50%,#5d6167)"></div>
  <div class="post-body"><div class="post-date">22 Feb, 2022</div><h3 class="post-title">Lorem ipsum dolor sit ame consectetuer adipi</h3><p class="post-ex">Lorem ipsum dolor sit amet, consectetuer adipiscing elit, sed diam nonummy nibh</p></div>
</article>
<div class="btn" style="left:540px;top:2417px;width:120px;height:36px">View All</div>

<!-- partners -->
<div class="partner" style="left:161px"><i></i>Corvel</div>
<div class="partner" style="left:340px"><i></i>Nordline</div>
<div class="partner" style="left:519px"><i></i>Palisa</div>
<div class="partner" style="left:698px"><i></i>Quintar</div>
<div class="partner" style="left:877px"><i></i>Bravik</div>

<!-- contact -->
<div class="sec-rule" style="top:2742px"></div>
<h2 class="sec-head display" style="top:2755px">Contact <span class="accent">Us</span></h2>

<div class="field" style="left:291px;top:2825px;width:300px;height:45px">
  <svg width="13" height="13" viewBox="0 0 14 14" fill="none" stroke="#138a9c" stroke-width="1.3"><circle cx="7" cy="4.5" r="3"/><path d="M1.5 13c.6-3 2.8-4.5 5.5-4.5s4.9 1.5 5.5 4.5"/></svg>Name</div>
<div class="field" style="left:609px;top:2825px;width:300px;height:45px">
  <svg width="13" height="13" viewBox="0 0 14 14" fill="none" stroke="#138a9c" stroke-width="1.3"><path d="M2 1.5h3l1.3 3-1.8 1.2a8 8 0 0 0 3.8 3.8l1.2-1.8 3 1.3v3C7 12.5 1.5 7 2 1.5Z"/></svg>Phone</div>
<div class="field" style="left:291px;top:2888px;width:300px;height:45px">
  <svg width="14" height="12" viewBox="0 0 14 12" fill="none" stroke="#138a9c" stroke-width="1.3"><rect x="1" y="1.5" width="12" height="9"/><path d="M1 2l6 5 6-5"/></svg>Email</div>
<div class="field" style="left:609px;top:2888px;width:300px;height:45px">
  <svg width="13" height="13" viewBox="0 0 14 14" fill="none" stroke="#138a9c" stroke-width="1.3"><path d="M2 12l1-3.5L10 1.5l2.5 2.5-7 7Z"/></svg>Company</div>
<div class="field" style="left:291px;top:2950px;width:618px;height:90px">
  <svg width="14" height="14" viewBox="0 0 14 14" fill="none" stroke="#138a9c" stroke-width="1.3"><rect x="1" y="2" width="10" height="11"/><path d="M6 9l1-3 5.5-5.5 1.3 1.3L8.3 7.3Z"/></svg>Message</div>
<div class="btn" style="left:532px;top:3077px;width:135px;height:37px">Submit Now</div>

<!-- footer -->
<nav class="fnav"><span class="active">Home</span><span>Services</span><span>Blog</span><span>Contact Us</span></nav>
<div class="social" style="left:891px"><i></i></div>
<div class="social" style="left:930px"><i></i></div>
<div class="social" style="left:969px"><i></i></div>
<div class="social" style="left:1008px"><i></i></div>
<div class="abs" style="left:161px;top:3289px;width:878px;height:1px;background:var(--line)"></div>

<div class="finfo" style="left:370px">
  <svg width="30" height="34" viewBox="0 0 30 34" fill="none" stroke="#0b3550" stroke-width="1.4"><path d="M15 31s-9-9-9-16a9 9 0 0 1 18 0c0 7-9 16-9 16Z"/><circle cx="15" cy="15" r="3.5"/></svg>
  <div>27, Rue des Tilleuls, Bât. C<br>69003 Lyon, France</div>
</div>
<div class="finfo" style="left:632px">
  <svg width="30" height="34" viewBox="0 0 30 34" fill="none" stroke="#0b3550" stroke-width="1.4"><path d="M5 6h6l2.5 6-3.5 2.4a16 16 0 0 0 7.6 7.6L20 18.5l6 2.5v6C15 28 4 17 5 6Z"/></svg>
  <div>Phone<br>+33 4 72 18 46 90</div>
</div>
<div class="finfo" style="left:829px">
  <svg width="30" height="34" viewBox="0 0 30 34" fill="none" stroke="#0b3550" stroke-width="1.4"><rect x="3" y="9" width="24" height="18"/><path d="M3 10l12 9 12-9"/></svg>
  <div>Email<br>info@etienneroubaud.fr</div>
</div>

<svg class="abs" style="left:0;top:3340px" width="1200" height="110">
  <rect x="0" y="43" width="1200" height="9" fill="#138a9c"/>
  <rect x="0" y="52" width="1200" height="58" fill="#0a2c43"/>
  <path d="M0 0H330L388 58V110H0Z" fill="#0b3550"/>
</svg>
<div class="brand" style="left:160px;top:3355px">
  <span class="brand-mark" style="border-color:#fff"></span>
  <div class="brand-name" style="color:#fff">Étienne Roubaud<small>CONSEIL</small></div>
</div>
<div class="copy">Copyright © 2022 Étienne Roubaud Conseil. All Rights Reserved. &nbsp;|&nbsp; Terms &amp; Conditions &nbsp;|&nbsp; Privacy Policies</div>

</body>
</html>
```